LumaMove In-home Personal Training

I would like to have some eye-catching business card design. Opened to any ideas.

The business idea: mobile fitness - train clients at their places

Target Market(s)

General population, 20-60 years old

Industry/Entity Type

Fitness

Contact Information for Business Card

The information to include:
Name: Marta
Call or text: 306-555-0187
Website: LumaMove.ca
Please use the attached logo

Requirements
Should not have
• No orange or purple colours please

```html
<!DOCTYPE html>
<html lang="en">
<head>
<meta charset="utf-8">
<title>LumaMove Business Card</title>
<link rel="stylesheet" href="https://fonts.googleapis.com/css2?family=Poppins:wght@300;400&display=swap">
<style>
  :root {
    --backdrop: #1b1b1c;
    --card-light: #ffffff;
    --card-dark: #3b3b3d;
    --ink-dark: #2f2f31;
    --ink-muted: #6a6a6c;
    --ink-light: #ffffff;
    --ink-light-muted: #d8d8d8;
  }
  * { box-sizing: border-box; margin: 0; padding: 0; }
  html, body {
    width: 1200px; height: 900px; overflow: hidden;
    background: var(--backdrop);
    font-family: "Poppins", sans-serif;
  }
  .sheet {
    width: 1200px; height: 900px;
    display: flex; flex-direction: column; align-items: center; justify-content: center;
    gap: 44px;
  }
  .card {
    width: 620px; height: 354px;
    display: flex; flex-direction: column; align-items: center; justify-content: center;
    box-shadow: 0 10px 30px rgba(0,0,0,.45);
  }
  .card--front { background: var(--card-light); color: var(--ink-dark); }
  .card--back { background: var(--card-dark); color: var(--ink-light); }

  .brand { display: flex; flex-direction: column; align-items: flex-end; }
  .brand__row { display: flex; align-items: center; gap: 16px; }
  .brand__dot {
    width: 40px; height: 40px; border-radius: 50%;
    border: 2px solid currentColor;
  }
  .brand__name {
    font-weight: 300; font-size: 46px; line-height: 1;
    letter-spacing: 8px;
  }
  .brand__tagline {
    font-weight: 300; font-size: 10.5px; letter-spacing: 3.6px;
    text-transform: uppercase; margin-top: 6px; margin-right: 6px;
  }
  .card--front .brand__tagline { color: var(--ink-muted); }
  .card--back .brand__tagline { color: var(--ink-light-muted); }

  .contact { margin-top: 34px; text-align: center; }
  .contact__name { font-size: 20px; font-weight: 400; letter-spacing: 1px; }
  .contact__line { font-size: 18px; font-weight: 400; margin-top: 4px; letter-spacing: .5px; }
  .contact__sep { display: inline-block; width: 7px; height: 7px; border-radius: 50%; background: currentColor; vertical-align: middle; margin: 0 8px; }

  .web {
    margin-top: 40px; font-size: 16px; font-weight: 400;
    letter-spacing: 8px; text-transform: uppercase;
  }
</style>
</head>
<body>
  <main class="sheet">
    <section class="card card--front">
      <div class="brand">
        <div class="brand__row">
          <span class="brand__dot"></span>
          <span class="brand__name">LumaMove</span>
        </div>
        <span class="brand__tagline">In-home Personal Training</span>
      </div>
      <div class="contact">
        <p class="contact__name">Marta</p>
        <p class="contact__line">306-555-0187<span class="contact__sep"></span>www.LumaMove.ca</p>
      </div>
    </section>

    <section class="card card--back">
      <div class="brand">
        <div class="brand__row">
          <span class="brand__dot"></span>
          <span class="brand__name">LumaMove</span>
        </div>
        <span class="brand__tagline">In-home Personal Training</span>
      </div>
      <p class="web">www.LumaMove.ca</p>
    </section>
  </main>
</body>
</html>
```